My Insurance Agency - R. T. Palloway Insurance Services Provides Insurance products to all of California. Most specifically the Bay Area.
"The Coverage Guy" is who I am advertising. providing Insurance solutions and consultations.
My Main Products are:
Life
Health
Disability
Accident
Employee Benefits
The colors of the card should match my uploaded logo.
I want the card to portray professionalism and security....Trust...and make people want to pick up the phone right now and make an appointment?
Target Market(s)
Young families, Seniors
Industry/Entity Type
Insurance
Look and feel
Each slider illustrates characteristics of the customer's brand and the style your logo design should communicate.

```html
<!DOCTYPE html>
<html lang="en">
<head>
<meta charset="utf-8">
<title>The Coverage Guy – Postcard</title>
<link href="https://fonts.googleapis.com/css2?family=Oswald:wght@600&family=Montserrat:wght@400;600;700&family=Didact+Gothic&family=Tinos&display=swap" rel="stylesheet">
<style>
  :root {
    --stage: #000000;
    --navy: #1d3766;
    --navy-deep: #16305c;
    --sky-light: #dbe7f3;
    --sky-mid: #9fb9d8;
    --grass: #b39a5c;
    --list-blue: #9cb9e6;
    --paper: #ffffff;
    --paper-warm: #fbf9f8;
    --line-grey: #8a8a8a;
    --stamp-grey: #9a9a9a;
  }
  * { margin: 0; padding: 0; box-sizing: border-box; }
  html, body { width: 1200px; height: 659px; overflow: hidden; background: var(--stage); }
  .canvas { position: relative; width: 1200px; height: 659px; background: var(--stage); }

  .card { position: absolute; top: 103px; height: 441px; background: var(--paper); overflow: hidden; }
  .card-front { left: 23px; width: 569px; }
  .card-back { left: 613px; width: 569px; }

  /* Front */
  .front-title {
    height: 110px; background: var(--navy); color: var(--paper);
    font-family: "Oswald", "Arial Narrow", sans-serif; font-weight: 600;
    font-size: 56px; letter-spacing: 2px; text-align: center; line-height: 112px;
  }
  .front-hero {
    position: relative; height: 219px;
    background: linear-gradient(180deg, var(--sky-mid) 0%, var(--sky-light) 55%, #e8e6da 78%, var(--grass) 88%, #8c7843 100%);
  }
  .front-tagline {
    position: absolute; left: 30px; top: 40px; color: var(--navy);
    font-family: "Didact Gothic", "Century Gothic", sans-serif; font-size: 27px; letter-spacing: 2px; line-height: 38px;
  }
  .front-tagline strong { font-family: "Montserrat", sans-serif; font-weight: 700; font-size: 25px; }
  .front-footer {
    position: relative; height: 112px; background: var(--paper-warm); color: var(--navy);
    font-family: "Montserrat", sans-serif;
  }
  .front-address { position: absolute; left: 30px; top: 22px; font-size: 14.5px; line-height: 20.5px; letter-spacing: .4px; }
  .front-address .name { font-weight: 700; }
  .brand-name {
    font-family: "Montserrat", sans-serif; font-weight: 700; color: var(--navy);
    text-transform: uppercase; letter-spacing: 1.5px; text-align: center;
  }
  .front-brand { position: absolute; left: 240px; top: 34px; width: 116px; font-size: 13px; line-height: 18px; }
  .front-contact { position: absolute; left: 366px; top: 22px; font-size: 13px; letter-spacing: .4px; }
  .front-contact li { list-style: none; display: flex; align-items: center; gap: 6px; height: 17px; }
  .front-contact li.phone { font-size: 18px; font-weight: 700; height: 25px; }
  .front-contact svg { flex: none; }

  /* Back */
  .back-panel { position: absolute; left: 0; top: 0; width: 275px; }
  .back-header {
    height: 93px; background: var(--navy); color: var(--paper);
    font-family: "Didact Gothic", "Century Gothic", sans-serif; font-size: 16px; letter-spacing: 1.2px;
    padding: 26px 0 0 22px; line-height: 18.5px;
  }
  .back-header strong { font-family: "Montserrat", sans-serif; font-weight: 600; font-size: 15px; }
  .back-photo { height: 74px; background: linear-gradient(180deg, #c9daf0 0%, #7fa3d3 60%, #5b84bf 100%); }
  .service-list {
    height: 130px; background: var(--list-blue); color: var(--navy-deep);
    font-family: "Montserrat", sans-serif; font-variant: small-caps; padding: 6px 0 0 30px;
  }
  .service-list h2 { font-size: 15px; font-weight: 700; letter-spacing: 1px; margin-bottom: 4px; }
  .service-list li { list-style: none; font-size: 15px; letter-spacing: 1px; line-height: 18.7px; display: flex; align-items: center; gap: 3px; }
  .back-contact { text-align: center; color: var(--navy); padding-top: 7px; }
  .back-contact .label { font-family: "Montserrat", sans-serif; font-variant: small-caps; font-size: 15px; letter-spacing: 1px; line-height: 18px; }
  .back-contact .phone { font-family: "Montserrat", sans-serif; font-weight: 700; font-size: 19px; letter-spacing: 1px; line-height: 22px; }
  .back-contact .web { font-family: "Tinos", "Times New Roman", serif; font-size: 13px; line-height: 12px; }
  .back-brand { position: absolute; left: 285px; top: 58px; width: 140px; font-size: 14px; line-height: 20px; }
  .stamp-box {
    position: absolute; left: 464px; top: 36px; width: 64px; height: 74px; border: 1px solid #b5b5b5;
    color: var(--stamp-grey); font-family: Arial, sans-serif; font-size: 12px; line-height: 14.5px;
    text-align: center; padding-top: 16px;
  }
  .address-line { position: absolute; left: 303px; width: 201px; height: 1px; background: var(--line-grey); }
</style>
</head>
<body>
<div class="canvas">

  <section class="card card-front">
    <header class="front-title">THE COVERAGE GUY</header>
    <div class="front-hero" role="img" aria-label="Photo of a businessman holding an umbrella over a man relaxing in an office chair in a grassy field under a blue sky">
      <p class="front-tagline">PROVIDING YOU<br><strong>INSURANCE SOLUTIONS</strong><br>AND <strong>CONSULATIONS</strong></p>
    </div>
    <footer class="front-footer">
      <div class="front-address">
        <div class="name">The Coverage Guy</div>
        <div>P.O Box - 4120</div>
        <div>Bayview Rd, CA 94010 USA</div>
      </div>
      <div class="brand-name front-brand">The Coverage Guy</div>
      <ul class="front-contact">
        <li class="phone">
          <svg width="8" height="16" viewBox="0 0 8 16"><path d="M6 1 C2 2 1 5 1 8 C1 11 2 14 6 15" fill="none" stroke="currentColor" stroke-width="2.2"/></svg>
          888-555-0142
        </li>
        <li>
          <svg width="10" height="8" viewBox="0 0 10 8"><rect x=".5" y=".5" width="9" height="7" fill="none" stroke="currentColor"/><path d="M.5 .5 L5 4.5 L9.5 .5" fill="none" stroke="currentColor"/></svg>
          hello@coverguyca.com
        </li>
        <li>
          <svg width="10" height="10" viewBox="0 0 10 10"><circle cx="5" cy="5" r="4.5" fill="none" stroke="currentColor"/><path d="M.5 5 H9.5 M5 .5 V9.5" stroke="currentColor" stroke-width=".8"/></svg>
          www.coverguyca.com
        </li>
      </ul>
    </footer>
  </section>

  <section class="card card-back">
    <div class="back-panel">
      <header class="back-header">PROVIDING YOU<br><strong>INSURANCE SOLUTIONS</strong><br>AND <strong>CONSULATIONS</strong></header>
      <div class="back-photo" role="img" aria-label="Close-up photo of a blue file folder tab labelled Insurance"></div>
      <div class="service-list">
        <h2>Services provided -</h2>
        <ul>
          <li><svg width="8" height="9" viewBox="0 0 8 9"><path d="M1 5 L3 8 L7 1" fill="none" stroke="currentColor" stroke-width="1.5"/></svg>Life</li>
          <li><svg width="8" height="9" viewBox="0 0 8 9"><path d="M1 5 L3 8 L7 1" fill="none" stroke="currentColor" stroke-width="1.5"/></svg>Health</li>
          <li><svg width="8" height="9" viewBox="0 0 8 9"><path d="M1 5 L3 8 L7 1" fill="none" stroke="currentColor" stroke-width="1.5"/></svg>Disability</li>
          <li><svg width="8" height="9" viewBox="0 0 8 9"><path d="M1 5 L3 8 L7 1" fill="none" stroke="currentColor" stroke-width="1.5"/></svg>Accident</li>
          <li><svg width="8" height="9" viewBox="0 0 8 9"><path d="M1 5 L3 8 L7 1" fill="none" stroke="currentColor" stroke-width="1.5"/></svg>Employee Benefits</li>
        </ul>
      </div>
      <div class="back-contact">
        <div class="label">Contact today</div>
        <div class="phone">888-555-0142</div>
        <div class="web">www.coverguyca.com</div>
      </div>
    </div>
    <div class="brand-name back-brand">The Coverage Guy</div>
    <div class="stamp-box">Place<br>Stamp<br>Here</div>
    <div class="address-line" style="top:222px"></div>
    <div class="address-line" style="top:262px"></div>
    <div class="address-line" style="top:304px"></div>
  </section>

</div>
</body>
</html>
```